Vermilion Reel Works Web Design

COMPANY: VERMILION REEL WORKS
LOCATION: SHANGHAI, CHINA
AREA: FILM/TV DRAMA/COMMERCIALS/GAME POST PRODUCTION, SOUND DESIGN, MUSIC, and GAME.
WEB STYLE: SIMPLE, PROFESSIONAL, TRUSTWORTHY

LANGUAGE: ENGLISH, CHINESE. (Same layout, different language)
UPDATE: AFTER PROJECT FINISHED, WE NEED UPDATE BY OURSELVES.

MAIN SUBJECT: 6
1 HOMEPAGE
2 ABOUT US
3 TEAM
4 SERVICES
5 FACILITY
6 CONTACT

add one page of JOB OPPORTUNITIES.

DETAILS
1 HOMEPAGE
SLOGAN: Vermilion Reel Works provides a well-designed working environment which amplifies your team’s ability to reach their creative goals.

Our services include:
 Feature Films
 Music & Scoring
 Commercials
 ADR & Foley
 Sound & Picture Editorial
 Sound Design
 Video Game

2 ABOUT US
Vermilion Reel Works is located in the premiere South-Bund area of Shanghai. Occupying a 5000 square meter Technical Building, Vermilion Reel Works was built by a filmmaker for filmmakers, and is one of the largest, most versatile full-service post-production facilities in China.

Vermilion Reel Works is positioning to be at the forefront of the latest technology. Our goal is to provide a comprehensive solution for the post-production needs of our clients. We offer two fully-equipped dubbing stages (one of which will be certified KESTRON VOXAR PREMIERE), a large variety of both picture and sound editing rooms, impressive Foley and ADR stages, a world-class scoring stage, and complete audio and video transfer services.

We can handle your entire project from editing all the way to the end of the final sound mix; all under one extremely comfortable roof. We fully realize that the true art is in listening to the needs of our clients and making their greatest vision a reality. To this end our creative team's expertise, with a network of sound supervisors, editors and mixers, will deliver the magic you need. Producers and directors will also find our richly appointed guest accommodations to be a comfortable and soothing place to wind up the day. Every aspect of your project will be taken care of by a skilled and dedicated team, in the way that is best suited to you.

3 TEAM
(attachment 01)

4 SERVICES
Sound Mix
ADR
FOLEY
MUSIC
Sound Design
Sound Edit
Picture Edit
for all the Films, TV Drama, Commercials, Video Games, Online Media
(attachment 02, use photo)

5 FACILITY
(attachment 03)

6 CONTACT
(attachment04)
with map

Project Deadline Extended
Reason: Designers work are great, my bosses will spend 1-2 days select one of these web design, and spend 1-2 days to make some change, maybe use new photos.

```html
<!DOCTYPE html>
<html lang="en">
<head>
<meta charset="utf-8">
<title>Vermilion Reel Works — About Us</title>
<link rel="stylesheet" href="https://fonts.googleapis.com/css2?family=Fjalla+One&family=Mulish:wght@400;500&display=swap">
<style>
  :root {
    --bg-dark: #232323;
    --bg-mid: #3a3a38;
    --band-blue: rgba(24, 128, 196, 0.72);
    --band-blue-soft: rgba(30, 140, 210, 0.45);
    --text: #f2f2f2;
    --muted: #c9d2da;
    --rule: rgba(255, 255, 255, 0.18);
    --pager-line: rgba(255, 255, 255, 0.45);
    --pager-active: #4aa3e0;
  }
  * { margin: 0; padding: 0; box-sizing: border-box; }
  html, body { width: 1200px; height: 600px; overflow: hidden; background: var(--bg-dark); }
  .page { position: relative; width: 1200px; height: 600px; overflow: hidden; }
  .hero-photo {
    position: absolute; inset: 0;
    background:
      radial-gradient(ellipse at 45% 35%, rgba(90, 88, 80, 0.55), transparent 60%),
      linear-gradient(180deg, var(--bg-mid) 0%, #2c2c2a 45%, var(--bg-dark) 100%);
  }
  .decor { position: absolute; inset: 0; }
  .menu-toggle { position: absolute; left: 247px; top: 23px; width: 19px; height: 15px; }
  .pager { position: absolute; right: 8px; top: 10px; width: 180px; }
  .pager-track { position: relative; height: 2px; background: var(--pager-line); }
  .pager-progress { position: absolute; left: 0; top: 0; width: 64px; height: 2px; background: var(--pager-active); }
  .pager-list { display: flex; justify-content: space-between; list-style: none; margin-top: 4px;
    font-family: "Mulish", sans-serif; font-size: 10px; color: var(--muted); padding-left: 22px; }
  .next-arrow { position: absolute; left: 1135px; top: 284px; width: 18px; height: 40px; }
  .about { position: absolute; left: 366px; top: 154px; width: 446px; color: var(--text); }
  .about-title { font-family: "Fjalla One", sans-serif; font-size: 34px; line-height: 1; letter-spacing: 0.2px; margin-bottom: 25px; }
  .about-text { font-family: "Mulish", sans-serif; font-size: 9.6px; line-height: 12px; margin-bottom: 12px; }
</style>
</head>
<body>
<main class="page">
  <div class="hero-photo" role="img" aria-label="Dark close-up of studio audio rack equipment with glowing buttons"></div>

  <svg class="decor" width="1200" height="600" viewBox="0 0 1200 600" aria-hidden="true">
    <polygon points="856,0 1200,0 1200,576" fill="var(--band-blue-soft)"/>
    <polygon points="972,0 1200,0 1200,352" fill="var(--band-blue)"/>
    <polygon points="0,252 200,600 0,600" fill="var(--band-blue-soft)"/>
    <polygon points="0,376 128,600 0,600" fill="var(--band-blue)"/>
    <g stroke="var(--rule)" stroke-width="0.8">
      <line x1="300" y1="0" x2="1200" y2="560"/>
      <line x1="860" y1="0" x2="300" y2="600"/>
      <line x1="0" y1="420" x2="1200" y2="140"/>
      <line x1="120" y1="0" x2="760" y2="600"/>
      <line x1="0" y1="520" x2="1200" y2="430"/>
      <line x1="1050" y1="0" x2="560" y2="600"/>
    </g>
  </svg>

  <svg class="menu-toggle" viewBox="0 0 19 15" aria-label="Menu" role="img">
    <g fill="#ffffff">
      <rect y="0" width="19" height="1.6"/><rect y="3.3" width="19" height="1.6"/>
      <rect y="6.6" width="19" height="1.6"/><rect y="9.9" width="19" height="1.6"/>
      <rect y="13.2" width="19" height="1.6"/>
    </g>
  </svg>

  <nav class="pager" aria-label="Sections">
    <div class="pager-track"><div class="pager-progress"></div></div>
    <ol class="pager-list">
      <li>01</li><li>02</li><li>03</li><li>04</li><li>05</li><li>06</li>
    </ol>
  </nav>

  <svg class="next-arrow" viewBox="0 0 18 40" aria-label="Next section" role="img">
    <polyline points="2,2 16,20 2,38" fill="none" stroke="#dfe6ec" stroke-width="2.4"/>
  </svg>

  <section class="about">
    <h1 class="about-title">ABOUT US</h1>
    <p class="about-text">Vermilion Reel Works is located in the premiere South-Bund area of Shanghai. Occupying a 5000 square meter Technical Building, Vermilion Reel Works was built by a filmmaker for filmmakers, and is one of the largest, most versatile full-service post-production facilities in China.</p>
    <p class="about-text">Vermilion Reel Works is positioning to be at the forefront of the latest technology. Our goal is to provide a comprehensive solution for the post-production needs of our clients. We offer two fully-equipped dubbing stages (one of which will be certified KESTRON VOXAR PREMIERE), a large variety of both picture and sound editing rooms, impressive Foley and ADR stages, a world-class scoring stage, and complete audio and video transfer services.</p>
    <p class="about-text">We can handle your entire project from editing all the way to the end of the final sound mix; all under one extremely comfortable roof. We fully realize that the true art is in listening to the needs of our clients and making their greatest vision a reality. To this end our creative team's expertise, with a network of sound supervisors, editors and mixers, will deliver the magic you need. Producers and directors will also find our richly appointed guest accommodations to be a comfortable and soothing place to wind up the day. Every aspect of your project will be taken care of by a skilled and dedicated team, in the way that is best suited to you.</p>
  </section>
</main>
</body>
</html>
```